Clear Plastic Card Design

I am looking to have a business card designed from my logo icon. I am looking to match the style of a different business card I have attached in the files.
Looking for a card that is plastic, with layers of transparency in the shape of my logo icon (also attached in the files) - not a circle like the other card. The winning design will incorporate the red icon logo on the front and back and include the charity's name, "Lanterns for the Weary" in the same or similar font, as well as an email and phone number. For now, use the email: email@lanternsfortheweary.org and the phone number 555-318-4072.
We like how the sample business card has transparency, partial and full opacity layers and a matching color scheme. Files will need to be in vector so that our business card printing company can work with it.
UPDATE:
We've some excellent designs in, thank you everyone! I got an early review from the owner, and he requested a minor redirect to find his perfect design. He wants the design to stand out by NOT being a rectangle. Try instead a circle, square, or best yet - something that falls in the outline of the logo icon, either fully or partially. Thank you, everyone!
Contact Information for Business Card
Lanterns for the Weary text should be incorporated as well as a phone and email.
Look and feel

```html
<!DOCTYPE html>
<html lang="en">
<head>
<meta charset="utf-8">
<title>Lanterns for the Weary – Business Card</title>
<link rel="stylesheet" href="https://fonts.googleapis.com/css2?family=Montserrat:wght@300;400;700&display=swap">
<style>
  :root {
    --stage-top: #c9c9c9;
    --stage-bottom: #ffffff;
    --card-crimson: #d81e4a;
    --card-red: #e0262f;
    --card-orange: #ea5a24;
    --card-deep: #c81f2a;
    --ink-white: #ffffff;
    --ink-black: #111111;
  }
  html, body {
    margin: 0;
    padding: 0;
    width: 1079px;
    height: 1200px;
    overflow: hidden;
  }
  body {
    background: linear-gradient(180deg, var(--stage-top) 0%, var(--stage-bottom) 100%);
  }
  .card-sheet {
    display: block;
    width: 1079px;
    height: 1200px;
  }
  .card-shadow { filter: drop-shadow(4px 8px 8px rgba(0,0,0,0.35)); }
  .front-face { fill: var(--card-crimson); }
  .org-heading {
    font-family: "Montserrat", sans-serif;
    font-weight: 700;
    font-size: 21px;
    fill: var(--ink-white);
    letter-spacing: 0.3px;
  }
  .contact-line {
    font-family: "Montserrat", sans-serif;
    font-weight: 300;
    font-size: 18px;
    fill: var(--ink-white);
  }
  .contact-icon { fill: var(--ink-white); }
  .brand-name-front {
    font-family: "Montserrat", sans-serif;
    font-weight: 700;
    font-size: 40px;
    fill: var(--ink-white);
  }
  .brand-name-back {
    font-family: "Montserrat", sans-serif;
    font-weight: 400;
    font-size: 20px;
    fill: var(--ink-black);
  }
  .brand-mark-back { fill: url(#mark-wash); }
  .back-panel { fill: #ffffff; }
</style>
</head>
<body>
<svg class="card-sheet" viewBox="0 0 960 1067" preserveAspectRatio="none" xmlns="http://www.w3.org/2000/svg">
  <defs>
    <path id="card-outline" d="M107,172 H305 V200 H460 V130 Q460,82 510,82 H560 Q590,82 600,100 H790 Q845,100 845,160 V420 Q845,480 790,480 H520 Q480,480 470,440 H135 Q107,440 107,412 Z"/>
    <linearGradient id="back-wash" x1="0" y1="0" x2="1" y2="1">
      <stop offset="0" stop-color="var(--card-crimson)"/>
      <stop offset="0.45" stop-color="var(--card-orange)"/>
      <stop offset="1" stop-color="var(--card-deep)"/>
    </linearGradient>
    <linearGradient id="mark-wash" x1="0" y1="0" x2="1" y2="1">
      <stop offset="0" stop-color="var(--card-crimson)"/>
      <stop offset="1" stop-color="var(--card-orange)"/>
    </linearGradient>
    <clipPath id="back-clip">
      <use href="#card-outline" transform="translate(0,485)"/>
    </clipPath>
  </defs>

  <!-- Front of card -->
  <g class="card-front">
    <use href="#card-outline" class="front-face card-shadow"/>
    <text class="org-heading" x="158" y="242">LANTERNS FOR</text>
    <text class="org-heading" x="158" y="270">THE WEARY</text>

    <path class="contact-icon" d="M161,314 q2,-2 4,0 l2,3 q1,2 -1,3 q1,3 4,4 q1,-2 3,-1 l3,2 q2,2 0,4 q-3,3 -8,-1 q-6,-5 -7,-10 z"/>
    <text class="contact-line" x="188" y="327">555-318-4072</text>

    <rect class="contact-icon" x="159" y="350" width="16" height="12" rx="1.5"/>
    <path d="M160,352 L167,357 L174,352" fill="none" stroke="var(--card-crimson)" stroke-width="1.6"/>
    <text class="contact-line" x="188" y="363">email@lanternsfortheweary.org</text>

    <text class="brand-name-front" text-anchor="middle">
      <tspan x="655" y="240">Lanterns</tspan>
      <tspan x="655" y="290">for the</tspan>
      <tspan x="655" y="340">Weary</tspan>
    </text>
  </g>

  <!-- Back of card -->
  <g class="card-back">
    <use href="#card-outline" transform="translate(0,485)" class="card-shadow" fill="var(--card-red)"/>
    <g clip-path="url(#back-clip)">
      <rect role="img" aria-label="Faceted red and orange low-poly backdrop" x="100" y="560" width="760" height="420" fill="url(#back-wash)"/>
      <path class="back-panel" d="M125,745 L180,705 Q300,700 420,680 Q560,655 600,625 Q640,640 660,650 Q780,660 815,690 Q840,740 800,790 L690,868 L640,868 L618,830 L596,868 L175,862 Z"/>
    </g>
    <rect class="brand-mark-back" x="512" y="700" width="100" height="100" rx="4"/>
    <text class="brand-name-back">
      <tspan x="353" y="808">Lanterns for the</tspan>
      <tspan x="353" y="834">Weary</tspan>
    </text>
  </g>
</svg>
</body>
</html>
```